Cedar Hall businesscard

We changed our name and logo, now we need new business cards.
3-4/72 Marlow Street Larkfield Vale 2199
www.cedarhall-example.org.au
info@cedarhall-example.org.au
Lorna-Jean Whitcombe
Senior Pastor
ph: 02 95874210

```html
<!DOCTYPE html>
<html lang="en">
<head>
<meta charset="utf-8">
<title>Cedar Hall business card</title>
<link rel="stylesheet" href="https://fonts.googleapis.com/css2?family=Arimo:wght@400;500&display=swap">
<style>
  :root {
    --page: #e9e7e4;
    --card: #ffffff;
    --accent-red: #d13a2e;
    --charcoal: #383b40;
    --ink: #2a2a2a;
    --rule: #2b2b2b;
    --slate: #6d8094;
  }
  * { margin: 0; padding: 0; box-sizing: border-box; }
  html, body {
    width: 1200px; height: 848px; overflow: hidden;
    background: var(--page);
    font-family: "Arimo", Arial, sans-serif;
  }
  .card {
    position: absolute; left: 100px; top: 134px;
    width: 1000px; height: 580px;
    background: var(--card);
    border-radius: 34px;
    overflow: hidden;
    box-shadow: 0 18px 40px rgba(0,0,0,0.18);
  }
  .card__swoosh { position: absolute; inset: 0; width: 100%; height: 100%; }
  .person {
    position: absolute; left: 96px; top: 58px; width: 600px;
  }
  .person__name {
    font-size: 46px; font-weight: 400; color: var(--accent-red);
    letter-spacing: 0.3px; line-height: 1; white-space: nowrap;
  }
  .person__role {
    font-size: 17px; color: var(--ink);
    margin-left: 230px; margin-top: 4px;
  }
  .contact {
    position: absolute; left: 120px; top: 178px; width: 560px;
    text-align: center; list-style: none;
    font-size: 22px; line-height: 1.3; color: var(--ink);
  }
  .divider {
    position: absolute; left: 730px; top: 46px;
    width: 2px; height: 360px; background: var(--rule);
  }
  .brand {
    position: absolute; left: 760px; top: 150px; width: 220px;
    display: flex; flex-direction: column; align-items: center; gap: 16px;
  }
  .brand__dot {
    width: 92px; height: 92px; border-radius: 50%;
    background: var(--slate);
  }
  .brand__name {
    font-size: 34px; font-weight: 400; color: var(--slate);
    letter-spacing: 1px; white-space: nowrap;
  }
</style>
</head>
<body>
  <article class="card">
    <svg class="card__swoosh" viewBox="0 0 1000 580" preserveAspectRatio="none" aria-hidden="true">
      <path fill="var(--accent-red)" d="M0 372 C 190 405, 390 480, 640 512 C 420 505, 200 445, 0 396 Z"/>
      <path fill="var(--charcoal)" d="M0 430 C 240 480, 480 555, 700 545 C 850 538, 930 480, 1000 455 L1000 580 L0 580 Z"/>
    </svg>

    <header class="person">
      <h1 class="person__name">Lorna-Jean Whitcombe</h1>
      <p class="person__role">Senior Pastor</p>
    </header>

    <ul class="contact">
      <li class="contact__phone">02 95874210</li>
      <li class="contact__web">www.cedarhall-example.org.au</li>
      <li class="contact__email">info@cedarhall-example.org.au</li>
      <li class="contact__address">3-4/72 Marlow Street Larkfield Vale 2199</li>
    </ul>

    <div class="divider"></div>

    <div class="brand">
      <span class="brand__dot"></span>
      <span class="brand__name">Cedar Hall</span>
    </div>
  </article>
</body>
</html>
```